Anzeigengestaltung für Heilpraktikerin für Psychotherapie
Hallo lorvik, ich bin sehr zufrieden mit dem Design. Danke LG Helga Brandner
Zielgruppe
Heilpraktikerin für Psychotherapie, Atem- und Körpertherapeutin, Einzelthearpie, Gruppentherapie, Menschen in Lebenskrisen; Menschen, die ihr Leben verändern wollen, Menschen suchen mehr Selbsterfahrung, vorwiegend Frauen, Atersgruppe 20 aufwärts, Menschen mit psychischen Problemen
Entspannung, Berühren, Massieren, Halten, Gespräch, Bewegen, Begleitung Während der Schwangerschaft, Geburt und danach, Trauerbegleitung
Aufgabenstellung
Name und Berufsbezeichnung sind mir wichtig
Praxiseröffnung, Termine nach Vereinbarung
aktuelles Angebot: Fantasiereise- Entspannung von Alltagsstress
sonstiges Angebot: Einzeltherapie/Gruppentherapie,

```html
<!DOCTYPE html>
<html lang="de">
<head>
<meta charset="utf-8">
<title>PraxisRaum – Anzeige</title>
<link href="https://fonts.googleapis.com/css2?family=Tenor+Sans&display=swap" rel="stylesheet">
<style>
:root{
  --stage:#d9d9d9;
  --paper:#ffffff;
  --magenta:#d6247f;
  --plum:#4a1c2e;
  --bullet:#9a8a90;
  --rose:#c9557a;
  --wine:#8e2c4a;
  --lilac:#d46fc8;
}
*{margin:0;padding:0;box-sizing:border-box}
html,body{width:1200px;height:676px;overflow:hidden}
body{
  background:radial-gradient(ellipse at 50% 45%,#f2f2f2 0%,var(--stage) 70%,#bdbdbd 100%);
  font-family:"Tenor Sans",sans-serif;
  color:var(--plum);
  position:relative;
}
.ad{
  position:absolute;left:375px;top:14px;width:450px;height:648px;
  background:var(--paper);overflow:hidden;
  box-shadow:0 10px 24px rgba(0,0,0,.25);
}
.ad__photo{
  position:absolute;right:0;top:0;width:310px;height:540px;
  background:
    radial-gradient(circle at 26% 32%,rgba(255,250,220,.95) 0%,rgba(255,190,90,.85) 12%,rgba(240,120,90,.55) 28%,rgba(255,255,255,0) 48%),
    radial-gradient(ellipse at 70% 40%,var(--wine) 0%,var(--rose) 35%,rgba(230,150,170,.5) 60%,rgba(255,255,255,0) 80%);
}
.ad__photo::after{
  content:"";position:absolute;inset:0;
  background:linear-gradient(90deg,#fff 0%,rgba(255,255,255,.6) 25%,rgba(255,255,255,0) 55%);
}
.ad__wave{
  position:absolute;left:0;top:445px;width:450px;height:120px;
  background:linear-gradient(180deg,rgba(255,255,255,0) 0%,rgba(212,111,200,.35) 45%,rgba(212,111,200,.2) 70%,rgba(255,255,255,0) 100%);
}
.brand{position:absolute;left:20px;top:58px;display:flex;align-items:center;gap:9px}
.brand__dot{width:14px;height:14px;border-radius:50%;background:var(--plum)}
.brand__name{font-size:27px;color:var(--plum);letter-spacing:.5px}
.headline{
  position:absolute;left:0;width:430px;top:114px;text-align:center;
  color:var(--magenta);font-size:29px;line-height:28px;font-weight:400;
}
.offer-intro{position:absolute;left:19px;top:198px;font-size:19px}
.offers{position:absolute;left:34px;top:242px;list-style:none;font-size:16.5px;line-height:25px}
.offers li{position:relative;padding-left:14px;margin-bottom:1.5px}
.offers li::before{
  content:"";position:absolute;left:0;top:11px;width:6px;height:6px;border-radius:50%;background:var(--bullet)
}
.current{position:absolute;left:20px;top:402px;font-size:15.5px;line-height:28px}
.contact{position:absolute;left:22px;top:546px;font-size:13.5px;line-height:22px;font-style:normal}
</style>
</head>
<body>
<main class="ad">
  <div class="ad__photo" role="img" aria-label="Foto einer Frau mit geschlossenen Augen im warmen Gegenlicht"></div>
  <div class="ad__wave" role="img" aria-label="Geschwungenes rosa-violettes Lichtband als Dekoration"></div>

  <div class="brand">
    <span class="brand__dot"></span>
    <span class="brand__name">PraxisRaum</span>
  </div>

  <h1 class="headline">Sie suchen<br>Ruhe und Erholung</h1>

  <p class="offer-intro">Ich biete Ihnen:</p>
  <ul class="offers">
    <li>Atem- und Körpertherapie</li>
    <li>Begleitung während der<br>Schwangerschaft, der Geburt und<br>der Zeit danach</li>
    <li>Gespräche</li>
    <li>Krisenbewältigung</li>
  </ul>

  <p class="current">Aktuelles Entspannungsangebot:<br>“Fantasiereise- Entspannung von Alltagsstress”</p>

  <address class="contact">
    Kontakt:<br>
    Lindenweg 14, 72661 Talheim | Tel.: 0170-12 34 56 7<br>
    EMail: praxisraum.helgabrandner@postfach.de<br>
    Homepage: www.praxisraum-brandner.org
  </address>
</main>
</body>
</html>
```